Business card for home decor store and design

I need a business card for my home decor boutique that’s professional looking boho/rustic. We sell vintage furniture, vintage finds, lamps, throws, rugs. We also carry a Diy paint line for refinishing furniture. We offer workshop on painting furniture, private or group setting. We in the heart of Old Town Red Bluff. We love to design, build and restore. Family owned small business. Our style is rustic boho farmhouse. We search for one of a kind found and repurposed items. We love vintage home decor, vintage windows.

Target Market(s)

Home decor

Industry/Entity Type

Home Accessories

Contact Information for Business Card

Have a rustic look/boho

Font styles to use
Serif
Script

Requirements
Must have
• Logo

```html
<!DOCTYPE html>
<html lang="en">
<head>
<meta charset="utf-8">
<title>Birch &amp; Loam Co. Business Card</title>
<link rel="stylesheet" href="https://fonts.googleapis.com/css2?family=Oswald:wght@500&family=Roboto:wght@300;400&display=swap">
<style>
  :root {
    --backdrop: #333333;
    --card: #232323;
    --ink: #f4f4f4;
    --ink-soft: #dcdcdc;
    --gloss: #3c3c3c;
    --gloss-text: #4a4a4a;
    --edge: #ffffff;
  }
  * { margin: 0; padding: 0; box-sizing: border-box; }
  html, body { width: 1200px; height: 901px; overflow: hidden; }
  body {
    background: var(--backdrop);
    font-family: "Roboto", Arial, sans-serif;
    color: var(--ink);
    position: relative;
  }
  .card {
    position: absolute;
    left: 270px;
    width: 660px;
    height: 377px;
    background: var(--card);
    overflow: hidden;
  }
  .card::after {
    content: "";
    position: absolute;
    left: 0; right: 0; bottom: 0;
    height: 7px;
    background: var(--edge);
  }
  .card--front { top: 52px; }
  .card--back { top: 472px; }

  /* Front */
  .front-mark {
    position: absolute;
    left: 50%; top: 150px;
    transform: translate(-50%, -50%);
    width: 200px; height: 200px;
    border: 4px solid var(--gloss);
    border-radius: 50%;
    display: flex; align-items: center; justify-content: center;
  }
  .front-mark__name {
    font-family: "Roboto", Arial, sans-serif;
    font-weight: 400;
    font-size: 26px;
    color: var(--gloss-text);
    white-space: nowrap;
  }
  .front-web {
    position: absolute;
    left: 0; right: 0; top: 300px;
    text-align: center;
    font-size: 19px;
    font-weight: 400;
    color: var(--ink-soft);
    letter-spacing: 0.3px;
  }

  /* Back */
  .brand {
    position: absolute;
    left: 60px; top: 70px;
    width: 180px; height: 180px;
    border: 4px solid var(--ink);
    border-radius: 50%;
    display: flex; align-items: center; justify-content: center;
  }
  .brand__name {
    font-family: "Roboto", Arial, sans-serif;
    font-weight: 400;
    font-size: 21px;
    color: var(--ink);
    white-space: nowrap;
  }
  .divider {
    position: absolute;
    left: 300px; top: 70px;
    width: 1px; height: 190px;
    background: var(--ink-soft);
  }
  .person {
    position: absolute;
    left: 338px; top: 72px;
  }
  .person__name {
    font-family: "Oswald", "Arial Narrow", sans-serif;
    font-weight: 500;
    font-size: 30px;
    letter-spacing: 1.5px;
    line-height: 1.1;
  }
  .person__role {
    font-size: 20px;
    font-weight: 300;
    color: var(--ink-soft);
    margin-top: 2px;
  }
  .contacts {
    list-style: none;
    margin-top: 22px;
  }
  .contacts__item {
    display: flex; align-items: center;
    font-size: 21px;
    font-weight: 400;
    height: 31px;
  }
  .contacts__icon {
    width: 18px; height: 18px;
    margin-right: 16px;
    flex: none;
  }
  .address {
    position: absolute;
    left: 150px; top: 310px;
    font-size: 21px;
    font-weight: 300;
    color: var(--ink-soft);
  }
</style>
</head>
<body>
  <section class="card card--front" aria-label="Card front">
    <div class="front-mark">
      <span class="front-mark__name">Birch &amp; Loam Co.</span>
    </div>
    <p class="front-web">www.yourwebsite.com</p>
  </section>

  <section class="card card--back" aria-label="Card back">
    <div class="brand">
      <span class="brand__name">Birch &amp; Loam Co.</span>
    </div>
    <div class="divider"></div>
    <div class="person">
      <h1 class="person__name">MARCUS HALE</h1>
      <p class="person__role">Manager</p>
      <ul class="contacts">
        <li class="contacts__item">
          <svg class="contacts__icon" viewBox="0 0 24 24" fill="none" stroke="#f4f4f4" stroke-width="2" stroke-linejoin="round"><path d="M5 3h4l2 5-2.5 1.5a11 11 0 0 0 6 6L16 13l5 2v4a2 2 0 0 1-2 2A16 16 0 0 1 3 5a2 2 0 0 1 2-2z"/></svg>
          123-456-2100
        </li>
        <li class="contacts__item">
          <svg class="contacts__icon" viewBox="0 0 24 24" fill="none" stroke="#f4f4f4" stroke-width="2" stroke-linejoin="round"><rect x="3" y="5" width="18" height="14"/><path d="M3 6l9 7 9-7"/></svg>
          youremail@mailbox.com
        </li>
        <li class="contacts__item">
          <svg class="contacts__icon" viewBox="0 0 24 24" fill="none" stroke="#f4f4f4" stroke-width="2"><circle cx="12" cy="12" r="9"/><path d="M3 12h18M12 3c3 3 3 15 0 18M12 3c-3 3-3 15 0 18"/></svg>
          www.yourwebsite.com
        </li>
      </ul>
    </div>
    <p class="address">Your address, city, state, ZIP 0000</p>
  </section>
</body>
</html>
```